Business card revamp

we are refrigeration mechanic i need a modern professional double side business card using my current branding
The card information must have site address~ 17 Whitlow st cobram, Vic 3644 postal address~ P.o. Box 862 cobram,Vic 3643 Phone Number~0358149637 Fax Nunber~0358260518 Email address~ brucet@pelvanor.com.au Title~ Manager Licence numbers~ AU47391, NSW 681329K Web site~ www.frostrimvane.com.au

Industry/Entity Type

Business

```html
<!DOCTYPE html>
<html lang="en">
<head>
<meta charset="utf-8">
<title>Business Card – Manager</title>
<link rel="stylesheet" href="https://fonts.googleapis.com/css2?family=Roboto+Condensed:wght@400;700&display=swap">
<style>
  :root {
    --card-blue: #2f7ef1;
    --ink-white: #ffffff;
  }
  html, body {
    margin: 0;
    padding: 0;
    overflow: hidden;
    background: var(--card-blue);
  }
  .card {
    position: relative;
    width: 1200px;
    height: 686px;
    background: var(--card-blue);
    color: var(--ink-white);
    font-family: "Roboto Condensed", "Arial Narrow", sans-serif;
    overflow: hidden;
  }
  .card__name {
    position: absolute;
    left: 94px;
    top: 66px;
    margin: 0;
    font-size: 92px;
    line-height: 92px;
    font-weight: 700;
    letter-spacing: 1px;
    text-transform: uppercase;
  }
  .card__role {
    position: absolute;
    left: 96px;
    top: 176px;
    margin: 0;
    font-size: 44px;
    line-height: 44px;
    font-weight: 400;
  }
  .card__rule {
    position: absolute;
    left: 96px;
    top: 245px;
    width: 914px;
    height: 4px;
    background: var(--ink-white);
  }
  .contact {
    position: absolute;
    left: 96px;
    top: 304px;
    margin: 0;
    padding: 0;
    list-style: none;
  }
  .contact__row {
    height: 69px;
    font-size: 46px;
    line-height: 46px;
    white-space: nowrap;
  }
  .contact__label {
    font-size: 32px;
    font-weight: 400;
    margin-right: 8px;
  }
  .contact__value {
    font-weight: 700;
    letter-spacing: 0.5px;
  }
  .contact__value--caps { text-transform: uppercase; }
  .contact__gap { display: inline-block; width: 26px; }
</style>
</head>
<body>
  <main class="card">
    <h1 class="card__name">Name Lastname</h1>
    <p class="card__role">Manager, Licence AU47391, NSW 681329K</p>
    <div class="card__rule"></div>
    <ul class="contact">
      <li class="contact__row"><span class="contact__label">site</span><span class="contact__value contact__value--caps">17 Whitlow st Cobram, Vic 3644</span></li>
      <li class="contact__row"><span class="contact__label">post</span><span class="contact__value contact__value--caps">PO Box 862 Cobram, Vic 3643</span></li>
      <li class="contact__row"><span class="contact__label">ph</span><span class="contact__value">0358149637</span><span class="contact__gap"></span><span class="contact__label">fax</span><span class="contact__value">0358260518</span></li>
      <li class="contact__row"><span class="contact__label">email</span><span class="contact__value">brucet@pelvanor.com.au</span></li>
      <li class="contact__row"><span class="contact__label">web</span><span class="contact__value">www.frostrimvane.com.au</span></li>
    </ul>
  </main>
</body>
</html>
```